Collaborative Law Bus Stop Bench Design

We are looking for a design for a bus stop bench-the size is 74 inches in length and 22 inches wide.We are a group of family law lawyers, social workers and accountants who are committed to resolving marital breakdowns without going to court.
As this is a bus stop ad not a lot of words can be used.
The sign needs to show our website www.tidewellhomecounsel.com prominently
We want the design to focus on the advantages of our process ie. not going to court-like"Don't air your dirty laundry"-a design with a clothesline or something like that.
It needs to be clear and uncomplicated but memorable.

```html
<!DOCTYPE html>
<html lang="en">
<head>
<meta charset="utf-8">
<title>Tidewell Home Counsel – Bench Designs</title>
<link rel="stylesheet" href="https://fonts.googleapis.com/css2?family=Barlow:wght@500;600;700;800;900&display=swap">
<style>
  :root {
    --ink: #000000;
    --paper: #ffffff;
    --red: #d40000;
    --yellow: #ffff00;
    --shadow: #3a3a3a;
  }
  * { margin: 0; padding: 0; box-sizing: border-box; }
  html, body {
    width: 1200px; height: 757px; overflow: hidden;
    background: var(--paper);
    font-family: "Barlow", Arial, sans-serif;
  }
  .canvas { position: relative; width: 1200px; height: 757px; }

  .bench { position: absolute; left: 20px; width: 1158px; background: var(--ink); }
  .bench--tunnel { top: 14px; height: 333px; }
  .bench--court { top: 362px; height: 335px; }

  .tunnel-field {
    position: absolute; left: 10px; top: 0; width: 1138px; height: 252px;
    background: radial-gradient(ellipse 560px 300px at 220px 160px, #ffffff 0%, #eeeeee 22%, #b0b0b0 50%, #555555 78%, #000000 100%);
  }
  .tunnel-brand {
    position: absolute; left: 170px; top: 132px;
    display: flex; align-items: center; gap: 10px;
  }
  .tunnel-brand-mark { width: 26px; height: 26px; background: var(--ink); flex: none; }
  .tunnel-brand-name {
    font-weight: 700; font-size: 19px; line-height: 21px; color: var(--ink);
  }
  .tunnel-headline {
    position: absolute; left: 42px; top: 13px; white-space: nowrap;
    font-weight: 900; font-size: 54px; letter-spacing: 0.4px; line-height: 1; color: var(--paper);
    text-shadow: 3px 3px 0 var(--shadow);
  }
  .tunnel-headline .glow { color: var(--yellow); }
  .tunnel-strap {
    position: absolute; right: 101px; top: 74px; white-space: nowrap;
    font-weight: 900; font-size: 81px; line-height: 1; color: var(--paper);
    text-shadow: 4px 4px 0 var(--shadow);
  }
  .tunnel-strap .court { color: var(--red); }
  .tunnel-copy {
    position: absolute; right: 106px; top: 170px; text-align: right; white-space: nowrap;
    font-weight: 700; font-size: 25px; letter-spacing: 0.3px; line-height: 32px; color: var(--paper);
    text-shadow: 2px 2px 0 var(--shadow);
  }
  .tunnel-copy em { font-style: italic; }

  .court-field {
    position: absolute; left: 8px; top: 8px; width: 1087px; height: 243px;
    background: var(--paper);
  }
  .court-judge {
    position: absolute; left: 20px; top: 16px; width: 305px; height: 235px;
    background: linear-gradient(180deg, #1a1a1a 0%, #000000 100%);
  }
  .court-plaque {
    position: absolute; left: 30px; top: 196px; width: 285px; height: 40px;
    display: flex; align-items: center; justify-content: center;
    font-weight: 700; font-size: 29px; color: var(--red);
  }
  .court-headline {
    position: absolute; left: 350px; top: 19px; white-space: nowrap;
    font-weight: 800; font-size: 94px; letter-spacing: 1px; line-height: 1; color: var(--red);
  }
  .court-answer {
    position: absolute; left: 350px; top: 108px; white-space: nowrap;
    font-weight: 700; font-size: 56px; letter-spacing: 0.5px; line-height: 1; color: var(--ink);
  }
  .court-answer .hit { color: var(--red); }
  .court-copy {
    position: absolute; left: 351px; top: 176px; white-space: nowrap;
    font-weight: 700; font-size: 25px; letter-spacing: 0.4px; line-height: 31px; color: var(--ink);
  }
  .court-copy .hit { color: var(--red); }

  .bench-url {
    position: absolute; right: 91px; bottom: 20px; white-space: nowrap;
    font-weight: 600; font-size: 47px; line-height: 1; color: var(--paper);
  }
</style>
</head>
<body>
<main class="canvas">

  <section class="bench bench--tunnel">
    <div class="tunnel-field"></div>
    <div class="tunnel-brand">
      <span class="tunnel-brand-mark"></span>
      <span class="tunnel-brand-name">Tidewell<br>Home Counsel</span>
    </div>
    <h1 class="tunnel-headline">Want to see <span class="glow">light</span> at the end of the tunnel?</h1>
    <p class="tunnel-strap">AND NOT <span class="court">COURT</span>!</p>
    <p class="tunnel-copy">At Tidewell Home Counsel we can make<br><em>YOUR</em> disputes, easier one’s, without getting lost on the way.</p>
    <p class="bench-url">www.tidewellhomecounsel.com</p>
  </section>

  <section class="bench bench--court">
    <div class="court-field"></div>
    <div class="court-judge" role="img" aria-label="Black silhouette illustration of a judge with a gavel seated at a high bench between two lamps"></div>
    <div class="court-plaque">The Big Cheese</div>
    <h2 class="court-headline">Silence in court!</h2>
    <p class="court-answer">Might just be the <span class="hit">Answer!</span></p>
    <p class="court-copy">At Tidewell Home Counsel we can make <span class="hit">YOUR</span> disputes,<br>easier one’s without having to face <span class="hit">The Big Cheese!</span></p>
    <p class="bench-url">www.tidewellhomecounsel.com</p>
  </section>

</main>
</body>
</html>
```